81M business card

I need a business card for a life sciences consulting firm I started. The company name is 81M and the logo is attached. I am looking for something edgey and current but different from the blah standard business card.

Industry/Entity Type

Business

Requirements
Nice to have
• Both sides

```html
<!DOCTYPE html>
<html lang="en">
<head>
<meta charset="utf-8">
<title>81M Business Card – Front and Back</title>
<link rel="stylesheet" href="https://fonts.googleapis.com/css2?family=Josefin+Sans:wght@300;400;600&family=Open+Sans:wght@400;600;700&display=swap">
<style>
  :root {
    --page-bg: #e9e7e4;
    --card-white: #ffffff;
    --card-black: #121212;
    --card-black-glow: #3a3a3a;
    --brand-blue: #233a8c;
    --brand-orange: #f08a1c;
    --tagline-grey: #6d6f73;
    --light-text: #f2f2f2;
    --muted-light: #c9c9c9;
  }
  * { box-sizing: border-box; margin: 0; padding: 0; }
  html, body {
    width: 1200px;
    height: 1000px;
    overflow: hidden;
    background: var(--page-bg);
  }
  .sheet {
    position: relative;
    width: 1200px;
    height: 1000px;
  }
  .card {
    position: absolute;
    left: 250px;
    width: 700px;
    height: 380px;
    overflow: hidden;
    box-shadow: 0 12px 30px rgba(0,0,0,0.18);
  }
  .card--front { top: 70px; background: var(--card-white); }
  .card--back {
    top: 530px;
    background: radial-gradient(ellipse 55% 70% at 50% 45%, var(--card-black-glow) 0%, var(--card-black) 75%);
    text-align: center;
  }

  /* Front */
  .front-mark {
    position: absolute;
    left: -90px;
    top: 100px;
    width: 300px;
    height: 300px;
    border-radius: 50%;
    background: var(--brand-blue);
  }
  .front-wordmark {
    position: absolute;
    left: 320px;
    top: 225px;
    font-family: "Open Sans", sans-serif;
    font-weight: 700;
    font-size: 78px;
    line-height: 1;
    letter-spacing: 2px;
    color: var(--brand-blue);
  }
  .front-wordmark .suffix { font-size: 26px; letter-spacing: 3px; margin-left: 4px; }
  .front-tagline {
    position: absolute;
    left: 322px;
    top: 322px;
    font-family: "Open Sans", sans-serif;
    font-weight: 400;
    font-size: 15px;
    color: var(--tagline-grey);
  }

  /* Back */
  .back-brand {
    display: flex;
    align-items: center;
    justify-content: center;
    gap: 14px;
    margin-top: 78px;
  }
  .back-mark {
    width: 54px;
    height: 54px;
    border-radius: 50%;
    background: var(--light-text);
  }
  .back-brand-text { text-align: left; }
  .back-wordmark {
    font-family: "Open Sans", sans-serif;
    font-weight: 700;
    font-size: 44px;
    line-height: 1;
    letter-spacing: 2px;
    color: var(--light-text);
  }
  .back-wordmark .suffix { font-size: 15px; letter-spacing: 2px; margin-left: 3px; }
  .back-tagline {
    font-family: "Open Sans", sans-serif;
    font-size: 9.5px;
    color: var(--muted-light);
    margin-top: 5px;
  }
  .person-name {
    font-family: "Josefin Sans", sans-serif;
    font-weight: 300;
    font-size: 30px;
    letter-spacing: 4px;
    color: var(--light-text);
    margin-top: 30px;
  }
  .person-role {
    font-family: "Josefin Sans", sans-serif;
    font-weight: 600;
    font-size: 11px;
    letter-spacing: 3px;
    color: var(--brand-orange);
    margin-top: 2px;
  }
  .contact-line {
    font-family: "Josefin Sans", sans-serif;
    font-weight: 400;
    font-size: 14px;
    letter-spacing: 2.5px;
    color: var(--muted-light);
  }
  .contact-line--phone { margin-top: 22px; }
  .contact-line--email { margin-top: 12px; font-size: 13px; }
</style>
</head>
<body>
  <main class="sheet">
    <section class="card card--front" aria-label="Card front">
      <div class="front-mark" aria-hidden="true"></div>
      <div class="front-wordmark">81M<span class="suffix">LLC</span></div>
      <p class="front-tagline">regulatory consulting and contract services</p>
    </section>

    <section class="card card--back" aria-label="Card back">
      <div class="back-brand">
        <div class="back-mark" aria-hidden="true"></div>
        <div class="back-brand-text">
          <div class="back-wordmark">81M<span class="suffix">LLC</span></div>
          <p class="back-tagline">regulatory consulting and contract services</p>
        </div>
      </div>
      <p class="person-name">Mara Ellison</p>
      <p class="person-role">MANAGER</p>
      <p class="contact-line contact-line--phone">0198 765 432</p>
      <p class="contact-line contact-line--email">mara@81m-consult.com</p>
    </section>
  </main>
</body>
</html>
```